Business card design for engineering firm specializing in defense industry.

We need a professional business card design. Something simple but stands out. We are an engineering company specializing in composites in the defense industry.
Industry/Entity Type
Defense
Contact Information for Business Card
A simple black business card with the Varlonix yellow color is what we had in mind but open for other designs.
Colors
ffc214

```html
<!DOCTYPE html>
<html lang="en">
<head>
<meta charset="utf-8">
<title>Varlonix business card</title>
<link rel="stylesheet" href="https://fonts.googleapis.com/css2?family=Montserrat:wght@400;500;800&display=swap">
<style>
  :root {
    --page-bg: #e1e3e2;
    --ink: #0d1520;
    --brand-yellow: #ffc214;
    --bright-yellow: #ffe01a;
    --text-white: #ffffff;
    --dot-yellow: #f2d21a;
  }
  * { margin: 0; padding: 0; box-sizing: border-box; }
  html, body {
    width: 992px; height: 1200px; overflow: hidden;
    background: var(--page-bg);
    font-family: "Montserrat", Arial, sans-serif;
  }
  .card {
    position: absolute; left: 94px; width: 806px; height: 460px;
    overflow: hidden; box-shadow: 0 2px 6px rgba(0,0,0,0.15);
  }
  .card-front { top: 101px; background: var(--bright-yellow); }
  .card-back { top: 618px; background: var(--ink); }
  .card-art { position: absolute; inset: 0; width: 100%; height: 100%; }
  .wordmark {
    position: absolute; color: var(--text-white);
    font-weight: 800; letter-spacing: 1px; white-space: nowrap; line-height: 1;
  }
  .front-wordmark { left: 0; right: 0; top: 182px; text-align: center; font-size: 82px; }
  .back-wordmark { left: 118px; top: 210px; font-size: 40px; }
  .divider {
    position: absolute; left: 381px; top: 170px; width: 3px; height: 118px;
    background: var(--text-white);
  }
  .contact-list { position: absolute; left: 432px; top: 0; list-style: none; }
  .contact-item {
    position: absolute; left: 0; display: flex; align-items: flex-start;
    color: var(--text-white); font-size: 17px; line-height: 23px; white-space: nowrap;
  }
  .contact-icon { width: 18px; height: 18px; margin-top: 2px; margin-right: 22px; flex: none; }
  .item-web { top: 151px; }
  .item-mail { top: 196px; }
  .item-phone { top: 239px; line-height: 20px; }
  .item-address { top: 294px; }
</style>
</head>
<body>

<section class="card card-front">
  <svg class="card-art" viewBox="0 0 1008 575" preserveAspectRatio="none">
    <defs>
      <radialGradient id="halftone-left" cx="0.5" cy="0.5" r="0.5">
        <stop offset="0" stop-color="#c9a010" stop-opacity="0.55"/>
        <stop offset="0.6" stop-color="#c9a010" stop-opacity="0.25"/>
        <stop offset="1" stop-color="#c9a010" stop-opacity="0"/>
      </radialGradient>
      <radialGradient id="halftone-right" cx="0.5" cy="0.5" r="0.5">
        <stop offset="0" stop-color="#e8c21a" stop-opacity="0.7"/>
        <stop offset="0.6" stop-color="#e8c21a" stop-opacity="0.3"/>
        <stop offset="1" stop-color="#e8c21a" stop-opacity="0"/>
      </radialGradient>
    </defs>
    <ellipse cx="60" cy="420" rx="170" ry="210" fill="url(#halftone-left)" role="img" aria-label="Halftone dot texture"/>
    <path class="dark-sweep" fill="var(--ink)"
      d="M462,0 L1008,0 L1008,40 C960,330 810,520 545,575 L0,575 L0,555 C60,250 230,55 462,0 Z"/>
    <path d="M462,0 C230,55 60,250 0,555" fill="none" stroke="#fff27a" stroke-width="3" opacity="0.35"/>
    <ellipse cx="975" cy="250" rx="170" ry="240" fill="url(#halftone-right)" role="img" aria-label="Halftone dot texture"/>
    <rect x="22" y="22" width="964" height="531" fill="none" stroke="var(--dot-yellow)" stroke-width="2" stroke-dasharray="2 10" opacity="0.55"/>
  </svg>
  <div class="wordmark front-wordmark">Varlonix</div>
</section>

<section class="card card-back">
  <svg class="card-art" viewBox="0 0 1008 575" preserveAspectRatio="none">
    <defs>
      <linearGradient id="swoop-fade" x1="0" y1="0" x2="0" y2="1">
        <stop offset="0" stop-color="var(--bright-yellow)" stop-opacity="0"/>
        <stop offset="0.55" stop-color="var(--bright-yellow)" stop-opacity="1"/>
      </linearGradient>
      <radialGradient id="halftone-back" cx="0.5" cy="0.5" r="0.5">
        <stop offset="0" stop-color="#b99a1a" stop-opacity="0.5"/>
        <stop offset="0.6" stop-color="#b99a1a" stop-opacity="0.2"/>
        <stop offset="1" stop-color="#b99a1a" stop-opacity="0"/>
      </radialGradient>
    </defs>
    <path fill="url(#swoop-fade)" d="M0,250 C20,430 120,545 265,575 L0,575 Z"/>
    <ellipse cx="1000" cy="330" rx="120" ry="280" fill="url(#halftone-back)" role="img" aria-label="Halftone dot texture"/>
    <rect x="22" y="22" width="964" height="531" fill="none" stroke="var(--dot-yellow)" stroke-width="2" stroke-dasharray="2 10" opacity="0.55"/>
  </svg>

  <div class="wordmark back-wordmark">Varlonix</div>
  <div class="divider"></div>

  <ul class="contact-list">
    <li class="contact-item item-web">
      <svg class="contact-icon" viewBox="0 0 20 20" fill="none" stroke="var(--brand-yellow)" stroke-width="1.3">
        <circle cx="10" cy="10" r="8.5"/><ellipse cx="10" cy="10" rx="3.8" ry="8.5"/>
        <line x1="1.5" y1="10" x2="18.5" y2="10"/><line x1="3" y1="5.5" x2="17" y2="5.5"/><line x1="3" y1="14.5" x2="17" y2="14.5"/>
      </svg>
      <span>www.varlonix.com</span>
    </li>
    <li class="contact-item item-mail">
      <svg class="contact-icon" viewBox="0 0 20 20">
        <rect x="2" y="5" width="16" height="11" fill="var(--brand-yellow)"/>
        <path d="M2,5 L10,11 L18,5" fill="none" stroke="var(--ink)" stroke-width="1.3"/>
      </svg>
      <span>Enquire@Varlonix.com</span>
    </li>
    <li class="contact-item item-phone">
      <svg class="contact-icon" viewBox="0 0 20 20">
        <path fill="var(--brand-yellow)" d="M4,1.5 L7,1.5 L8.5,6 L6.5,7.8 C7.6,10.2 9.6,12.3 12.2,13.5 L14,11.5 L18.5,13 L18.5,16 C18.5,17.5 17.3,18.5 16,18.5 C8.3,18 2,11.7 1.5,4 C1.5,2.7 2.5,1.5 4,1.5 Z"/>
      </svg>
      <span>+420 555 014 839<br>+420 555 014 350</span>
    </li>
    <li class="contact-item item-address">
      <svg class="contact-icon" viewBox="0 0 20 20">
        <path fill="var(--brand-yellow)" d="M10,0.5 C6.2,0.5 3.5,3.3 3.5,7 C3.5,11.5 10,19.5 10,19.5 C10,19.5 16.5,11.5 16.5,7 C16.5,3.3 13.8,0.5 10,0.5 Z"/>
        <circle cx="10" cy="7" r="2.5" fill="var(--ink)"/>
      </svg>
      <span>Varlonix PLUS, spol. s r.o.<br>Lipová 220 Brodec 34001<br>Czech Republic</span>
    </li>
  </ul>
</section>

</body>
</html>
```